EXPEDITE! Business Card For a Private Equity Firm
Fresh and Sleek
EXPEDITE!  Business Card For a Private Equity Firm - Financial Services
Creative Brief
Bright & Fun-filled
Ned Rusholt
Managing Partner
712 Larkmoor Street New York, NY 10032
ned@vorumbra-example.com
www.vorumbra-example.com
Looking for a fresh look on our new business cards. We have had previous designs on Plenavox for similar companies, but, now is time to refresh the look! Please submit as many design as possible. We will give you fast, efficient feedback!
Vorumbra Vorumbra
All. We also need email signatures and letterhead. Please provide.

```html
<!DOCTYPE html>
<html lang="en">
<head>
<meta charset="utf-8">
<title>Vorumbra Business Card</title>
<link rel="stylesheet" href="https://fonts.googleapis.com/css2?family=Cinzel:wght@500&family=Open+Sans:wght@300;400;600&display=swap">
<style>
  :root {
    --bg: #e4e4e2;
    --card: #f7f8f9;
    --brand-blue: #1f6fb0;
    --panel-blue: #1d5d9a;
    --panel-light: #3f8fd0;
    --panel-dark: #2a2d31;
    --text-light: #eaf3fb;
    --text-grey: #5d6a75;
    --sky-top: #e9eff3;
    --sky-mid: #c6d3dc;
    --sky-low: #9eb2c0;
  }
  * { margin: 0; padding: 0; box-sizing: border-box; }
  html, body { width: 1200px; height: 840px; overflow: hidden; }
  body {
    background: var(--bg);
    font-family: "Open Sans", Arial, sans-serif;
    position: relative;
  }
  .card {
    position: absolute;
    left: 270px;
    width: 660px;
    height: 377px;
    background: var(--card);
    overflow: hidden;
    box-shadow: 0 6px 18px rgba(0,0,0,.18);
  }
  .card-front { top: 28px; }
  .card-back { top: 435px; }

  .skyline {
    position: absolute; inset: 0;
    background: linear-gradient(180deg, var(--sky-top) 0%, var(--sky-mid) 55%, var(--sky-low) 100%);
  }
  .front-logo {
    position: absolute; left: 0; right: 0; top: 120px;
    display: flex; align-items: center; justify-content: center; gap: 18px;
  }
  .logo-dot {
    width: 48px; height: 48px; border-radius: 50%;
    background: var(--brand-blue);
  }
  .logo-name {
    font-family: "Cinzel", "Times New Roman", serif;
    font-weight: 500;
    color: var(--brand-blue);
    letter-spacing: 2px;
  }
  .front-logo .logo-name { font-size: 66px; }
  .front-url {
    position: absolute; right: 28px; bottom: 26px;
    font-family: "Cinzel", "Times New Roman", serif;
    font-size: 15px; letter-spacing: 1px;
    color: var(--panel-dark);
  }

  .back-shapes { position: absolute; inset: 0; }
  .contact {
    position: absolute; left: 30px; top: 40px;
    color: var(--text-light);
    font-weight: 300;
  }
  .contact-name { font-size: 19px; font-weight: 400; }
  .contact-title { font-size: 11px; margin-top: 2px; opacity: .85; }
  .contact-list { list-style: none; margin-top: 26px; font-size: 11px; line-height: 1.65; }
  .contact-list li { display: flex; align-items: center; gap: 7px; }
  .contact-list svg { width: 10px; height: 10px; flex: none; }
  .contact-address { display: block; }
  .back-logo {
    position: absolute; left: 300px; top: 188px;
    display: flex; flex-direction: column; align-items: center; gap: 10px;
  }
  .back-logo .logo-dot { width: 40px; height: 40px; }
  .back-logo .logo-name { font-size: 46px; }
</style>
</head>
<body>

<section class="card card-front">
  <div class="skyline" role="img" aria-label="Soft pale blue photograph of a city skyline seen through office windows"></div>
  <div class="front-logo">
    <span class="logo-dot"></span>
    <span class="logo-name">VORUMBRA</span>
  </div>
  <p class="front-url">WWW.VORUMBRA-EXAMPLE.COM</p>
</section>

<section class="card card-back">
  <svg class="back-shapes" viewBox="0 0 660 377" width="660" height="377" aria-hidden="true">
    <defs>
      <linearGradient id="panelGrad" x1="0" y1="0" x2="1" y2="1">
        <stop offset="0" stop-color="#3f8fd0"/>
        <stop offset="1" stop-color="#174f86"/>
      </linearGradient>
    </defs>
    <polygon points="0,0 330,0 230,377 0,377" fill="#2a2d31"/>
    <polygon points="0,0 300,0 196,260 0,300" fill="url(#panelGrad)"/>
  </svg>

  <div class="contact">
    <p class="contact-name">Ned Rusholt</p>
    <p class="contact-title">Managing Partner</p>
    <ul class="contact-list">
      <li>
        <svg viewBox="0 0 10 10"><path d="M5 0a3.5 3.5 0 0 0-3.5 3.5C1.5 6 5 10 5 10s3.5-4 3.5-6.5A3.5 3.5 0 0 0 5 0zm0 5a1.5 1.5 0 1 1 0-3 1.5 1.5 0 0 1 0 3z" fill="currentColor"/></svg>
        <span class="contact-address">712 Larkmoor Street<br>New York, NY 10032</span>
      </li>
      <li>
        <svg viewBox="0 0 10 10"><path d="M2 0h2l1 2.5-1.3 1a6 6 0 0 0 2.8 2.8l1-1.3L10 6v2a2 2 0 0 1-2 2A8 8 0 0 1 0 2a2 2 0 0 1 2-2z" fill="currentColor"/></svg>
        <span>T: (212) 555-0148</span>
      </li>
      <li>
        <svg viewBox="0 0 10 10"><path d="M2 0h2l1 2.5-1.3 1a6 6 0 0 0 2.8 2.8l1-1.3L10 6v2a2 2 0 0 1-2 2A8 8 0 0 1 0 2a2 2 0 0 1 2-2z" fill="currentColor"/></svg>
        <span>F: (212) 555-0149</span>
      </li>
      <li>
        <svg viewBox="0 0 10 10"><path d="M0 2h10v6H0z" fill="none" stroke="currentColor"/><path d="M0 2l5 3.5L10 2" fill="none" stroke="currentColor"/></svg>
        <span>ned@vorumbra-example.com</span>
      </li>
    </ul>
  </div>

  <div class="back-logo">
    <span class="logo-dot"></span>
    <span class="logo-name">VORUMBRA</span>
  </div>
</section>

</body>
</html>
```